Webdesign für Reisebüro
Zielgruppe
Reisebüro - wir haben uns vor 20 Jahren auf Reisen nach Asien spezialisiert aber inzwischen ist unsere Kernkompetenz das individuelle Arrangieren von Fernreisen in alle Welt. Jedoch decken wir auch das komplette touristische Portfolio ab was natürlich auch nicht zu kurz kommen darf. Unsere Zielgruppe liegt tatsächlich zwischen 20—70
Aufgabenstellung
Wir bezeichnen uns als das besondere Reisebüro weil wir als Menschen besonders sind. Wir lieben es zu begeistern und das gelingt uns so gut dass wir seit bestimmt 15 Jahren komplett ohne Werbung auskommen und nur von Mundpropaganda leben. Das Design soll genau dieses Besondere zum Ausdruck bringen. Soll keine „klassische“ Reisebüroseite sein auf der man selbst Reisen suchen Und buchen kann.
Natürlich wird es zb eine Seite „Über uns“ und Zielgebietsinfos und noch andere Seiten geben. Primär geht es jetzt mal um das Design an sich das unser Programmierer dann sicher umsetzen kann.
Das Büro ist bisschen im Factory Style eingerichtet und wird aktuell noch mehr diesem Style angepasst.
Der Name Maple Nook spiegelt den chilligen Lifestyle wieder den wir verkörpern.

```html
<!DOCTYPE html>
<html lang="de">
<head>
<meta charset="utf-8">
<title>Maple Nook – Reisen</title>
<link href="https://fonts.googleapis.com/css2?family=Raleway:ital,wght@0,300;0,400;1,300&family=Satisfy&family=Dancing+Script:wght@600&display=block" rel="stylesheet">
<style>
  :root {
    --band: #96bec2;
    --ink: #4a4f56;
    --text: #2f3236;
    --light: #ececec;
    --white: #ffffff;
    --dark-tab: #55595e;
    --ring: #4d5156;
    --script-teal: #7a9ea2;
    --script: "Satisfy", "Dancing Script", cursive;
  }
  * { margin: 0; padding: 0; box-sizing: border-box; }
  html, body { width: 676px; height: 1200px; overflow: hidden; background: var(--white); }
  body { font-family: "Raleway", Arial, sans-serif; font-weight: 300; color: var(--ink); position: relative; }
  .page { position: relative; width: 676px; height: 1200px; }

  .topbar { position: absolute; top: 0; left: 0; width: 676px; height: 15px; background: var(--white);
    font-size: 4.6px; font-style: italic; color: #666; }
  .topbar .hours { position: absolute; left: 10px; top: 5px; }
  .topbar .mail { position: absolute; right: 40px; top: 5px; color: #2d4b78; }

  .hero { position: absolute; top: 15px; left: 0; width: 676px; height: 353px;
    background:
      radial-gradient(ellipse 38% 55% at 50% 72%, rgba(240,240,242,0.95) 0%, rgba(225,226,228,0.6) 55%, rgba(225,226,228,0) 100%),
      linear-gradient(180deg, #5b83b3 0%, #9fb7d2 18%, #e3e6ea 40%, #d6d8dc 58%, #8e9a86 78%, #3c5529 100%); }
  .navband { position: absolute; top: 68px; left: 0; width: 676px; height: 63px;
    background: rgba(255,255,255,0.42); border-top: 1px solid rgba(255,255,255,0.7); border-bottom: 1px solid rgba(255,255,255,0.7); }
  .brand { position: absolute; left: 32px; top: 30px; width: 122px; height: 122px; border-radius: 50%;
    background: #f3f1ee; border: 2px solid var(--ring); display: flex; align-items: center; justify-content: center; }
  .brand span { font-family: "Raleway", Arial, sans-serif; font-weight: 400; font-size: 17px; color: var(--ink); }
  .page-title { position: absolute; left: 201px; top: 86px; font-size: 26px; font-weight: 300; letter-spacing: 0.5px; color: var(--ink); }
  .mainnav { position: absolute; top: 94px; font-size: 10.5px; color: var(--ink); }
  .mainnav a { position: absolute; white-space: nowrap; color: inherit; text-decoration: none; }
  .side-tab { position: absolute; left: 654px; top: 160px; width: 22px; height: 95px; background: var(--dark-tab);
    display: flex; align-items: center; justify-content: center; }
  .side-tab span { transform: rotate(-90deg); color: var(--white); font-size: 12px; font-weight: 400; white-space: nowrap; }

  .band { position: absolute; left: 0; width: 676px; background: var(--band); display: flex; align-items: center; justify-content: center; }
  .band h2 { font-family: var(--script); font-weight: 400; font-size: 29px; color: var(--ink); line-height: 1; }

  .destinations { position: absolute; top: 423px; left: 0; width: 676px; height: 224px; background: var(--light); }
  .dest { position: absolute; top: 21px; width: 150px; }
  .dest .ring { width: 149px; height: 149px; border-radius: 50%; border: 2.5px solid var(--ring);
    display: flex; align-items: center; justify-content: center; }
  .dest .photo { width: 120px; height: 120px; border-radius: 50%; }
  .dest h3 { position: absolute; top: 173px; left: 0; width: 160px; text-align: center; font-size: 13px; font-weight: 300; color: var(--ink); }

  .about { position: absolute; top: 703px; left: 0; width: 676px; height: 262px; background: var(--white); }
  .about .kicker { position: absolute; left: 67px; top: 57px; font-family: var(--script); font-size: 12px; color: var(--script-teal); }
  .about p { position: absolute; font-size: 8.6px; line-height: 10.2px; color: var(--text); font-weight: 300; white-space: nowrap; }
  .about .left { left: 69px; top: 106px; }
  .about .right { left: 496px; top: 67px; }
  .about .interior { position: absolute; left: 254px; top: 8px; width: 175px; height: 232px;
    background:
      radial-gradient(ellipse 30% 10% at 55% 18%, rgba(255,255,250,0.9), rgba(255,255,250,0) 100%),
      linear-gradient(180deg, #9fcfb0 0%, #d3cdc3 8%, #e2dbd0 30%, #8d7a63 55%, #b79b7c 70%, #b06e48 100%);
    box-shadow: 3px 3px 6px rgba(0,0,0,0.35); }

  .tagline { top: 965px; height: 57px; }
  .tagline p { font-size: 12.5px; color: var(--white); font-weight: 300; }

  .blog { position: absolute; top: 1022px; left: 0; width: 676px; height: 178px;
    background: linear-gradient(180deg, #4c586b 0%, #4b5669 50%, #3f4756 75%, #353b46 100%); text-align: center; }
  .blog h2 { font-family: var(--script); font-weight: 400; font-size: 30px; color: var(--white); margin-top: 16px; line-height: 1; }
  .blog .rule { width: 353px; height: 1px; background: rgba(255,255,255,0.55); margin: 18px auto 0; }
  .blog p { font-size: 16px; font-style: italic; font-weight: 300; color: var(--white); margin-top: 9px; }
</style>
</head>
<body>
<div class="page">
  <header class="topbar">
    <span class="hours">Tel: 0821 - 4410298 &nbsp;&nbsp;&nbsp;&nbsp; ÖFFNUNGSZEITEN: &nbsp;MO-FR &nbsp;10 - 13 h / 14 - 18 h &nbsp;&nbsp; SA &nbsp;10 - 13 h &nbsp;- &nbsp;Mi Vormittag geschlossen</span>
    <span class="mail">✉ &nbsp;info@maple-nook.example</span>
  </header>

  <section class="hero" role="img" aria-label="Weißer Tempel in Thailand unter bewölktem Himmel">
    <div class="navband"></div>
    <div class="brand"><span>Maple Nook</span></div>
    <h1 class="page-title">REISEN</h1>
    <nav class="mainnav">
      <a style="left:372px">ÜBER UNS</a>
      <a style="left:440px">KONTAKT</a>
      <a style="left:498px">IMPRESSUM</a>
      <a style="left:568px">DATENSCHUTZ</a>
    </nav>
    <div class="side-tab"><span>KONTAKT</span></div>
  </section>

  <div class="band" style="top:368px;height:55px"><h2>Ihr Reisebüro in Augsburg</h2></div>

  <section class="destinations">
    <div class="dest" style="left:21px">
      <div class="ring"><div class="photo" role="img" aria-label="Longtail-Boot vor Felsen in Thailand" style="background:linear-gradient(160deg,#5f7f55 0%,#8ab9c4 45%,#6fa9b5 60%,#8a5a3a 100%)"></div></div>
      <h3>THAILAND</h3>
    </div>
    <div class="dest" style="left:183px">
      <div class="ring"><div class="photo" role="img" aria-label="Brücke in New York am Abend" style="background:linear-gradient(180deg,#8796b0 0%,#c7a07c 50%,#a07656 65%,#3f4a5c 100%)"></div></div>
      <h3>USA</h3>
    </div>
    <div class="dest" style="left:347px">
      <div class="ring"><div class="photo" role="img" aria-label="Berge, Wald und See in Kanada" style="background:linear-gradient(180deg,#d0d9e2 0%,#7d8e86 35%,#4f7048 50%,#8e9ea4 60%,#8ea64a 100%)"></div></div>
      <h3>KANADA</h3>
    </div>
    <div class="dest" style="left:509px">
      <div class="ring"><div class="photo" role="img" aria-label="Violette Seerose in Sri Lanka" style="background:radial-gradient(circle at 60% 40%,#a070d0 0%,#7a5a9a 20%,#3c4a3a 55%,#22281f 100%)"></div></div>
      <h3>SRI LANKA</h3>
    </div>
  </section>

  <div class="band" style="top:647px;height:56px"><h2>Über uns</h2></div>

  <section class="about">
    <div class="kicker">Wer wir sind</div>
    <p class="left">Das Maple Nook in Augsburg ist<br>ein inhabergeführtes Reisebüro<br>im Herzen von Augsburg.<br>Bei uns werden Sie individuell<br>und sehr ausführlich beraten,<br>damit Ihre Reiseplanungen<br>garantiert zum Erfolg werden.</p>
    <div class="interior" role="img" aria-label="Einrichtung des Reisebüros mit Holzkommode und Lampe"></div>
    <p class="right">Wir freuen uns wenn Sie das<br>Maple Nook besuchen.<br>Unsere Spezialgebiet sind Reisen<br>in all asiatischen Länder wie<br>Thailand, Vietnam, China und Indien,<br>aber wir sind auf der ganzen Welt<br>zu Hause.<br>Egal ob eine Städtereise in Europa,<br>&nbsp;ein Trip in die USA oder Kanada, oder<br>der Event zum nächsten Heimspiel<br>Ihres Lieblingsvereins.</p>
  </section>

  <div class="band tagline"><p>Wir machen Ihre Reise zu einem unvergesslichen Erlebnis.</p></div>

  <section class="blog" role="img" aria-label="Nächtliche Stadtsilhouette im Hintergrund">
    <h2>blog</h2>
    <div class="rule"></div>
    <p>Reisetipps und Empfehlungen</p>
  </section>
</div>
</body>
</html>
```